Business Card: RW Office Partners - Your tidy answer finder

Business Name: RW Office Partners
Website: www.rwofficepartners.com.au
Email: marisol@rwofficepartners.com.au
Mobile: 61 487 902 346
Facebook: @rwofficepartners
Instrgram: @rwofficepartners

Brading Colours:
HEX
#986474
#ddccd3
#7a8498
#c9d8e4
#000000
#ffffff

Tag Line: Your tidy answer finder

Link to DRAFT website:
https://helpdeskhub.sitebuilderx.com/rw-office-partners

About Page from the website:
My name is Marisol Bramwell, and I would love to assist you to become more productive in your day to day and achieve your business and personal goals.
My mission is to give you time, time to work on the important tasks of your business or to be able to spend more time with your family. I will take on the tasks you don’t have time for, don’t know well or simply don’t like to do.
I have an extensive background in Administration, Tender Coordination, Document Control, WHS and Quality Management working primarily in the Construction, Mining and Corporate World.
I am passionate about being organised, having order and making things in your life (and mine) easier! I love to watch something unfold and grow into something amazing! I am known for being the go-to problem solver, the organiser of all things, producing high standards of work even under pressure. I’m also a confident communicator, and I understand that you’re busy running your business.

Target Market(s)

Small to Medium Business who require assistance in their business by a virtual assistant.

Industry/Entity Type

Virtual Assistant

Contact Information for Business Card

Mobile: 61 487 902 346

Font styles to use
Sans Serif

Colors
ffffff

Requirements
Must have
• Branding Colours as outlined.
Contact Details as outlined.
Logo as provided.
Proper contact details - mobile, facebook, instragm, website.
Simple, Elegant, very clean looking.
Should not have
• Note cute with pictures.
Not too girly as still want to market to construction companies.

```html
<!DOCTYPE html>
<html lang="en">
<head>
<meta charset="utf-8">
<title>RW Office Partners – Business Card</title>
<link href="https://fonts.googleapis.com/css2?family=Arimo:wght@400;700&display=swap" rel="stylesheet">
<style>
  :root {
    --plum: #986474;
    --blush: #ddccd3;
    --slate: #7a8498;
    --mist: #c9d8e4;
    --ink: #000000;
    --paper: #ffffff;
    --backdrop: #eeeeef;
  }
  * { box-sizing: border-box; margin: 0; padding: 0; }
  html, body {
    width: 1200px;
    height: 770px;
    overflow: hidden;
    background: var(--backdrop);
    font-family: "Arimo", Arial, sans-serif;
  }
  .sheet {
    position: relative;
    width: 1200px;
    height: 770px;
  }
  .card {
    position: absolute;
    width: 500px;
    height: 290px;
    background: var(--paper);
    box-shadow: 0 2px 4px rgba(0,0,0,0.06), 0 14px 30px rgba(0,0,0,0.08);
  }
  .card--front { left: 60px; top: 240px; }
  .card--back  { left: 640px; top: 240px; }

  .brand {
    display: flex;
    align-items: center;
    gap: 12px;
  }
  .brand__mark {
    flex: none;
    width: 22px;
    height: 22px;
    background: var(--plum);
  }
  .brand__name {
    font-size: 30px;
    font-weight: 400;
    color: var(--slate);
    letter-spacing: 0.5px;
    white-space: nowrap;
  }

  .card--front .brand {
    position: absolute;
    left: 50%;
    top: 50%;
    transform: translate(-50%, -50%);
  }

  .card--back .details {
    position: absolute;
    left: 50%;
    top: 50%;
    transform: translate(-50%, -50%);
    width: 300px;
  }
  .card--back .brand__name { font-size: 24px; }
  .card--back .brand__mark { width: 18px; height: 18px; }
  .tagline {
    margin: 5px 0 0 30px;
    font-size: 11px;
    color: var(--slate);
    white-space: nowrap;
  }
  .contact {
    margin: 14px 0 0 30px;
    list-style: none;
    font-size: 12px;
    line-height: 1.5;
    color: var(--slate);
    white-space: nowrap;
  }
  .contact__name {
    font-weight: 700;
    font-size: 13px;
    color: var(--plum);
    text-transform: uppercase;
    letter-spacing: 0.3px;
    margin-bottom: 2px;
  }
  .contact__label {
    color: var(--plum);
    font-weight: 700;
    margin-right: 4px;
  }
</style>
</head>
<body>
  <main class="sheet">
    <section class="card card--front" aria-label="Card front">
      <div class="brand">
        <span class="brand__mark" aria-hidden="true"></span>
        <span class="brand__name">RW Office Partners</span>
      </div>
    </section>

    <section class="card card--back" aria-label="Card back">
      <div class="details">
        <div class="brand">
          <span class="brand__mark" aria-hidden="true"></span>
          <span class="brand__name">RW Office Partners</span>
        </div>
        <p class="tagline">Your tidy answer finder</p>
        <ul class="contact">
          <li class="contact__name">Marisol Bramwell</li>
          <li class="contact__phone"><span class="contact__label">M</span>61 487 902 346</li>
          <li class="contact__email"><span class="contact__label">E</span>marisol@rwofficepartners.com.au</li>
          <li class="contact__web"><span class="contact__label">W</span>www.rwofficepartners.com.au</li>
          <li class="contact__facebook"><span class="contact__label">Facebook</span>@rwofficepartners</li>
          <li class="contact__instagram"><span class="contact__label">Instagram</span>@rwofficepartners</li>
        </ul>
      </div>
    </section>
  </main>
</body>
</html>
```